Rural photograpy business card design

I need a business card for my photography business, brianna delys photography. I would like my logo and pre designed font used on the card. Also my business specialises in photographing rural australia (e.g. shearing sheds, livestock, landscapes, farms), so a rural or country feel to the card would be great. I would like to keep the colours fresh but not too overpowering or juvenile.
Updates

Hi,

Could you please add my facebook page to the card - www.snapfolio-example.com/Brianna/Delys/Photography.
Thanks,
Brianna.

Reason: I have uploaded two photos I would like either one used on the card.

Target Market(s)

Farmers, country people from their mid twenties onwards

Industry/Entity Type

Business

Contact Information for Business Card

Brianna Delys Photography. Brianna Pemberton. 5182 Yarrowby-Tullagong Road, Wirrabin Qld 4491. 0471602394.

Requirements
Must have
• My pre-designed logo and font. Also please add my facebook address - www.snapfolio-example.com/BriannaDelys/Photography.
Please use one of the photos I have provided.
Should not have
• Peoples faces on the card.

```html
<!DOCTYPE html>
<html lang="en">
<head>
<meta charset="utf-8">
<title>Brianna Delys Photography – Business Card</title>
<link href="https://fonts.googleapis.com/css2?family=Quicksand:wght@500&display=swap" rel="stylesheet">
<style>
  :root {
    --backdrop: #d9d6d1;
    --kraft: #a88a5c;
    --kraft-light: #b09465;
    --ink: #1c1712;
    --band-dark: #241a12;
    --band-mid: #3a2b1e;
    --band-text: #9c8669;
  }
  * { margin: 0; padding: 0; box-sizing: border-box; }
  html, body {
    width: 1200px;
    height: 1000px;
    overflow: hidden;
    background: var(--backdrop);
    font-family: "Quicksand", sans-serif;
  }
  .card {
    position: absolute;
    left: 100px;
    top: 195px;
    width: 1000px;
    height: 610px;
    background: linear-gradient(160deg, var(--kraft-light), var(--kraft));
    color: var(--ink);
    box-shadow: 0 10px 30px rgba(0,0,0,0.25);
    overflow: hidden;
  }
  .brand {
    position: absolute;
    left: 70px;
    top: 150px;
    width: 320px;
    text-align: center;
  }
  .brand-mark {
    display: block;
    margin: 0 auto 22px;
  }
  .brand-name {
    font-size: 34px;
    font-weight: 500;
    letter-spacing: 3px;
    line-height: 1.25;
    text-transform: uppercase;
    color: var(--ink);
  }
  .divider {
    position: absolute;
    left: 425px;
    top: 130px;
    width: 2px;
    height: 290px;
    background: linear-gradient(to bottom, transparent, var(--ink) 20%, var(--ink) 80%, transparent);
    opacity: 0.8;
  }
  .contact {
    position: absolute;
    left: 465px;
    top: 165px;
    font-weight: 500;
  }
  .contact-name {
    font-size: 46px;
    letter-spacing: 1px;
    margin-bottom: 10px;
  }
  .contact-line {
    font-size: 31px;
    line-height: 1.3;
  }
  .texture-band {
    position: absolute;
    left: 0;
    bottom: 0;
    width: 100%;
    height: 150px;
    background: linear-gradient(100deg, var(--band-mid), var(--band-dark) 45%, var(--band-mid) 75%, var(--band-dark));
  }
  .web-address {
    position: absolute;
    right: 60px;
    bottom: 105px;
    font-size: 22px;
    font-weight: 500;
    color: var(--band-text);
    letter-spacing: 0.5px;
  }
</style>
</head>
<body>
  <main class="card">
    <div class="brand">
      <svg class="brand-mark" width="70" height="70" viewBox="0 0 70 70" aria-hidden="true">
        <circle cx="35" cy="35" r="30" fill="none" stroke="#1c1712" stroke-width="4"/>
      </svg>
      <div class="brand-name">Brianna Delys<br>Photography</div>
    </div>

    <div class="divider"></div>

    <section class="contact">
      <div class="contact-name">Brianna Pemberton</div>
      <div class="contact-line">5182 Yarrowby-Tullagong Road</div>
      <div class="contact-line">Wirrabin Qld 4491</div>
      <div class="contact-line">0471602394</div>
    </section>

    <div class="texture-band" role="img" aria-label="Dark weathered timber texture band"></div>
    <div class="web-address">www.snapfolio-example.com/Brianna/Delys/Photography</div>
  </main>
</body>
</html>
```